Create a banner for me that embodies my health and well being package.

I am an intuitive counselor with a busy practice helping clients to shift their blocks and move forward in their lives.
I have created a package called '9 paths home again'
I am wanting a banner to put on my website page, facebook page and to use as a letter head in mailouts.
My ideal clients are those who want to create change in their lives and who invest money in themselves and their personal and spiritual growth.
I am different to regular life coaches as my sessions have a spiritual twist to them creating much deeper change in my clients.
I would like the banner to be mainly font with the title of the progam: 9 Paths Home Again (no other wording) (something along the lines of the Blackjack font) and that ties in with the theme of my website. I'm not sure what else I want with it and am looking for ideas.
Website:
www.quillorabalancecare.com.au
I also have a current facebook page for the business:
https://www.facebook.com/Quillora-Balance-Care-402715938846102/
(Note: I am about to drop my logo and business name and move to using my own name - the rest of the website will remain the same).
I have attached a doc with the draft of what wording will be on the website page any advertising will link to, to give you an idea of what the program is about.

Target Market(s)

People who invest money on themselves who are looking to improve their emotional well being and creating change in their life. Majority are middle aged women (also younger females and some men)

Industry/Entity Type

Health And Wellness

Font styles to use
Other font styles liked:
• I like Blackjack and Amienne. Along those lines.

Requirements
Must have
• Attractive, modern and GREAT font.
Nice to have
• Surprise me with something amazing!
• I love the colours in the 2 images I have up loaded as they represent the heart chakra colours. They could be a feature on the banner or blurred into the background.
Should not have
• Even though my work is quite spiritual I don't want it to look woo woo (meaning airy fairy spiritual stuff!)

```html
<!DOCTYPE html>
<html lang="en">
<head>
<meta charset="utf-8">
<title>Quillora Balance Care</title>
<link rel="stylesheet" href="https://fonts.googleapis.com/css2?family=Questrial&family=Dancing+Script:wght@700&display=swap">
<style>
  :root {
    --bamboo-dark: #2f4a1c;
    --bamboo-mid: #6f8a3a;
    --bamboo-light: #a5b56a;
    --page: #ffffff;
    --sage: #b9cfa6;
    --brand-text: #6b6a9c;
    --nav-shade: rgba(10, 40, 0, 0.78);
    --leaf-green: #3b8f0f;
    --lotus-pink: #ee4fae;
    --lotus-red: #e4123c;
    --band: #000000;
    --band-line: #57c417;
    --card: #676699;
    --white: #ffffff;
  }
  * { box-sizing: border-box; margin: 0; padding: 0; }
  html, body { width: 1200px; height: 871px; overflow: hidden; }
  body {
    position: relative;
    font-family: "Questrial", Arial, sans-serif;
    background: linear-gradient(90deg, var(--bamboo-dark) 0%, var(--bamboo-mid) 5%, var(--bamboo-light) 10%, var(--bamboo-mid) 50%, var(--bamboo-light) 90%, var(--bamboo-dark) 100%);
  }
  .page {
    position: absolute; left: 94px; top: 9px; width: 1008px; height: 862px;
    background: var(--page);
  }
  .brand {
    position: absolute; left: 0; right: 0; top: 9px;
    display: flex; flex-direction: column; align-items: center;
  }
  .brand-mark {
    width: 108px; height: 108px; border-radius: 50%; background: var(--sage);
  }
  .brand-name {
    margin-top: 12px; font-size: 22px; color: var(--brand-text); letter-spacing: 0.5px;
  }
  .hero {
    position: absolute; left: 26px; top: 175px; width: 957px; height: 361px; overflow: hidden;
    background:
      radial-gradient(ellipse 260px 200px at 50% 58%, var(--lotus-red) 0%, var(--lotus-pink) 45%, rgba(238,79,174,0) 100%),
      radial-gradient(ellipse 420px 260px at 48% 62%, #f7a9d9 0%, rgba(247,169,217,0) 80%),
      linear-gradient(90deg, #123d06 0%, var(--leaf-green) 45%, #7fc51a 85%, #2f6d0a 100%);
  }
  .main-nav {
    position: absolute; left: 0; top: 0; width: 100%; height: 59px;
    background: var(--nav-shade);
  }
  .main-nav a {
    position: absolute; top: 10px; color: var(--white); text-decoration: none;
    font-family: Arial, Helvetica, sans-serif; font-size: 16px; line-height: 19px;
  }
  .program-band {
    position: absolute; left: 0; top: 262px; width: 100%; height: 76px;
    background: var(--band);
    border-top: 2px solid var(--band-line); border-bottom: 2px solid var(--band-line);
    display: flex; align-items: center; justify-content: center;
  }
  .program-title {
    font-family: "Dancing Script", cursive; font-weight: 700; font-size: 36px;
    color: var(--white);
    text-shadow: 0 0 3px var(--lotus-red), 0 0 8px var(--lotus-red);
  }
  .card {
    position: absolute; top: 557px; width: 300px; height: 287px;
  }
  .card-photo { height: 155px; }
  .card-body {
    height: 132px; background: var(--card); color: var(--white); text-align: center;
    padding-top: 10px;
  }
  .card-title { font-size: 24px; font-weight: 400; line-height: 28px; }
  .card-rule { width: 48px; height: 2px; background: var(--white); margin: 8px auto 10px; }
  .card-text { font-size: 13.5px; line-height: 22px; }
  .photo-stones { background: radial-gradient(circle at 50% 50%, #5a4a3a 0 8%, #b8c3cc 30%, #8d9aa6 100%); }
  .photo-lotus { background: radial-gradient(ellipse at 65% 45%, #f072b8 0 14%, #1c2b18 40%, #0a0f08 100%); }
  .photo-petals { background: linear-gradient(180deg, #6f6875 0%, #958c98 50%, #c59c8a 75%, #8a7a76 100%); }
</style>
</head>
<body>
  <main class="page">
    <header class="brand">
      <span class="brand-mark" aria-hidden="true"></span>
      <span class="brand-name">quillora balance care</span>
    </header>

    <section class="hero" role="img" aria-label="Close-up photograph of a pink lotus flower on a soft green background">
      <nav class="main-nav">
        <a href="#" style="left:36px">home</a>
        <a href="#" style="left:151px">consultations</a>
        <a href="#" style="left:320px">workshops</a>
        <a href="#" style="left:473px">about<br>rosalind</a>
        <a href="#" style="left:620px">happy<br>clients</a>
        <a href="#" style="left:758px">blog</a>
        <a href="#" style="left:865px">contact</a>
      </nav>
      <div class="program-band">
        <h1 class="program-title">9 Paths Home Again</h1>
      </div>
    </section>

    <article class="card" style="left:24px">
      <div class="card-photo photo-stones" role="img" aria-label="Photograph of pebbles arranged in a spiral"></div>
      <div class="card-body">
        <h2 class="card-title">consultations</h2>
        <div class="card-rule"></div>
        <p class="card-text">consultations to shift<br>the things that are<br>holding you back</p>
      </div>
    </article>

    <article class="card" style="left:354px">
      <div class="card-photo photo-lotus" role="img" aria-label="Photograph of a pink water lily with goldfish in a pond"></div>
      <div class="card-body">
        <h2 class="card-title">workshops</h2>
        <div class="card-rule"></div>
        <p class="card-text">a range of<br>weekend workshops<br>to help you grow</p>
      </div>
    </article>

    <article class="card" style="left:684px">
      <div class="card-photo photo-petals" role="img" aria-label="Photograph of a bowl of dried rose petals before a stone statue"></div>
      <div class="card-body">
        <h2 class="card-title">make a booking</h2>
        <div class="card-rule"></div>
        <p class="card-text">book in with Rosalind<br>to create the change<br>you are looking for</p>
      </div>
    </article>
  </main>
</body>
</html>
```